first fantastic look and impression

We are looking for a concept for letterhead, business card, emailfooter and template for invoices or offers for our company in the consultation business.
The dancer is a symbol who we are: it looks simple, but there is a lot of hard work and many years of training in this movement. The look is also what we want: elegant, modern, strong, with a touch of extravaganza
Target Market(s)
Hotelbusiness , Consulting
Font styles to use
Sans Serif
Other font styles liked:
- please give us a option we are open
Requirements
Must have
- We are not typical consultants but sparring partners and coaches for the hotel and that should also be expressed in the design. Maybe there is an icon that supports the whole thing. We are more modern and bolder than our industry colleagues.
we are modern, fresh, agile, fast
Nice to have
- a icon

```html
<!DOCTYPE html>
<html lang="en">
<head>
<meta charset="utf-8">
<title>Brightwell+Company – Invoice and Letterhead</title>
<link href="https://fonts.googleapis.com/css2?family=Montserrat:wght@400;500;600&family=Open+Sans:wght@400&family=Roboto:wght@400&display=swap" rel="stylesheet">
<style>
  :root {
    --bg: #dedede;
    --paper: #ffffff;
    --ink: #14151f;
    --text: #4a4a4f;
    --muted: #6b6b70;
    --rule: #5a5a60;
    --row-light: #f2f2f4;
    --row-dark: #e6e6e9;
    --accent: #3f5f4d;
  }
  * { box-sizing: border-box; margin: 0; padding: 0; }
  html, body { width: 1200px; height: 800px; overflow: hidden; background: var(--bg); }
  body { position: relative; font-family: "Montserrat", sans-serif; color: var(--ink); }

  .sheet { position: absolute; background: var(--paper); }
  .sheet--invoice { left: 164px; top: 111px; width: 412px; height: 574px; }
  .sheet--letter { left: 613px; top: 110px; width: 407px; height: 574px; }

  .brand { position: absolute; display: flex; align-items: center; gap: 5px;
    font-family: "Montserrat", sans-serif; font-weight: 600; color: var(--ink);
    letter-spacing: 0.08em; white-space: nowrap; }
  .brand__mark { width: 9px; height: 9px; background: var(--ink); }
  .brand--invoice { left: 27px; top: 54px; font-size: 9.5px; }
  .brand--letter { left: 0; right: 0; top: 63px; justify-content: center; font-size: 10px; }

  .contact { list-style: none; font-family: "Roboto", sans-serif; color: var(--text); }
  .contact li { display: flex; align-items: center; gap: 4px; white-space: nowrap; }
  .icon { width: 8px; height: 8px; fill: var(--ink); flex: none; }

  .contact--header { position: absolute; left: 261px; top: 32px; font-size: 8.6px; line-height: 11px; }
  .contact--header .plain { display: block; }

  .invoice-title { position: absolute; left: 27px; top: 119px; font-size: 11.5px; font-weight: 600; letter-spacing: 0.02em; }
  .date-label { position: absolute; left: 302px; top: 124px; font-size: 7px; font-weight: 500; color: var(--accent); }

  .field { position: absolute; left: 27px; right: 27px; display: flex; align-items: flex-end; gap: 4px;
    font-size: 7px; font-weight: 500; color: var(--muted); }
  .field__line { flex: 1; border-bottom: 0.8px solid var(--rule); height: 8px; }
  .field--customer { top: 137px; }
  .field--address { top: 154px; }
  .field--phone { top: 170px; }
  .field--phone .field__line.short { flex: 0 0 155px; margin-right: 4px; }

  .items { position: absolute; left: 27px; top: 195px; width: 358px; height: 273px;
    border: 0.8px solid var(--rule); }
  .items__head { display: grid; grid-template-columns: 47px 187px 62px 1fr; height: 22px; background: var(--ink); }
  .items__head span { display: flex; align-items: center; justify-content: center;
    color: #fff; font-size: 8.2px; font-weight: 500; border-right: 0.8px solid #fff; }
  .items__head span:last-child { border-right: none; }
  .items__body { display: grid; grid-template-columns: 47px 187px 62px 1fr; height: 250px;
    background: repeating-linear-gradient(to bottom, var(--row-light) 0 20.8px, var(--row-dark) 20.8px 41.6px); }
  .items__body span { border-right: 0.8px solid var(--rule); }
  .items__body span:last-child { border-right: none; }

  .totals { position: absolute; left: 260px; top: 468px; width: 125px;
    border: 0.8px solid var(--rule); border-top: none; }
  .totals__row { display: grid; grid-template-columns: 62px 1fr; height: 21px; border-top: 0.8px solid var(--rule); }
  .totals__row span { display: flex; align-items: center; padding-left: 9px; font-size: 7px; font-weight: 500; }
  .totals__row span + span { border-left: 0.8px solid var(--rule); }

  .payment { position: absolute; left: 27px; top: 480px; display: flex; gap: 13px; list-style: none;
    font-size: 7px; font-weight: 500; color: var(--muted); }
  .payment li { display: flex; align-items: center; gap: 3px; }
  .payment li::before { content: ""; width: 7px; height: 7px; border: 0.8px solid var(--muted); }

  .terms { position: absolute; left: 27px; top: 509px; font-size: 7px; line-height: 10.5px; color: var(--muted); }

  .letter-body { position: absolute; left: 37px; width: 334px; top: 129px;
    font-family: "Open Sans", sans-serif; font-size: 7.3px; line-height: 11px; color: var(--text); }
  .letter-body p { text-align: justify; margin-bottom: 11px; }
  .letter-body .greeting, .letter-body .closing { text-align: left; }
  .signature { position: absolute; left: 37px; top: 421px; width: 48px; height: 46px;
    background: linear-gradient(135deg, #f4f4f5, #e4e4e7); }

  .contact--footer { position: absolute; left: 37px; top: 508px; font-size: 9.4px; line-height: 13px; }
  .contact--footer .icon { width: 9px; height: 9px; }
  .address-footer { position: absolute; right: 36px; top: 510px; text-align: right;
    font-family: "Roboto", sans-serif; font-size: 9.4px; line-height: 12px; color: var(--text); font-style: normal; }
  .address-footer strong { font-weight: 400; color: var(--ink); }
</style>
</head>
<body>
<svg width="0" height="0" style="position:absolute" aria-hidden="true">
  <defs>
    <symbol id="i-phone" viewBox="0 0 24 24"><path d="M6.6 10.8a15 15 0 0 0 6.6 6.6l2.2-2.2a1 1 0 0 1 1-.25 11.4 11.4 0 0 0 3.6.57 1 1 0 0 1 1 1V20a1 1 0 0 1-1 1A17 17 0 0 1 3 4a1 1 0 0 1 1-1h3.5a1 1 0 0 1 1 1c0 1.25.2 2.45.57 3.57a1 1 0 0 1-.25 1z"/></symbol>
    <symbol id="i-mail" viewBox="0 0 24 24"><path d="M2 5h20v14H2z M4 7v.5l8 5.5 8-5.5V7z" fill-rule="evenodd"/></symbol>
    <symbol id="i-web" viewBox="0 0 24 24"><path d="M12 2a10 10 0 1 0 0 20 10 10 0 0 0 0-20zm0 2a8 8 0 0 1 7.7 6H15l-3-4zm-6 3.5L9 12l-3 4.5A8 8 0 0 1 6 7.5zM12 20l-3-4h5l4 2.5A8 8 0 0 1 12 20z"/></symbol>
  </defs>
</svg>

<section class="sheet sheet--invoice" aria-label="Invoice">
  <div class="brand brand--invoice"><span class="brand__mark"></span>BRIGHTWELL+COMPANY</div>
  <ul class="contact contact--header">
    <li class="plain">48 Larkspur Lane,</li>
    <li class="plain">Fernvale, ON K2P 4R7</li>
    <li><svg class="icon"><use href="#i-phone"/></svg>+15550142788</li>
    <li><svg class="icon"><use href="#i-mail"/></svg>hello@brightwellcompany.com</li>
    <li><svg class="icon"><use href="#i-web"/></svg>www.brightwellcompany.com</li>
  </ul>

  <h1 class="invoice-title">INVOICE # :</h1>
  <div class="date-label">DATE :</div>
  <div class="field field--customer">Customer :<span class="field__line"></span></div>
  <div class="field field--address">Address :<span class="field__line"></span></div>
  <div class="field field--phone">Phone :<span class="field__line short"></span>Fax :<span class="field__line"></span></div>

  <div class="items">
    <div class="items__head"><span>QTY</span><span>DESCRIPTION</span><span>PRICE</span><span>AMOUNT</span></div>
    <div class="items__body"><span></span><span></span><span></span><span></span></div>
  </div>

  <div class="totals">
    <div class="totals__row"><span>SUB TOTAL</span><span></span></div>
    <div class="totals__row"><span>GST #</span><span></span></div>
    <div class="totals__row"><span>SUBTOTAL</span><span></span></div>
  </div>

  <ul class="payment">
    <li>VISA</li><li>MC</li><li>DEBIT</li><li>CASH</li><li>CHEQUE</li>
  </ul>
  <p class="terms">Signature Indicates<br>Acceptance of Price and term</p>
</section>

<section class="sheet sheet--letter" aria-label="Letterhead">
  <div class="brand brand--letter"><span class="brand__mark"></span>BRIGHTWELL+COMPANY</div>
  <div class="letter-body">
    <p class="greeting">Dear customer,</p>
    <p>Lorem ipsum dolor sit amet, consectetur adipisicing elit, sed do eiusmod tempor incididunt ut labore et dolore magna aliqua. Ut enim ad minim veniam, quis nostrud exercitation ullamco laboris nisi ut aliquip ex ea commodo consequat. Duis aute irure dolor in reprehenderit in voluptate velit esse cillum dolore eu fugiat nulla pariatur. Excepteur sint occaecat cupidatat non proident, sunt in culpa qui officia deserunt mollit anim id est laborum.</p>
    <p>Lorem ipsum dolor sit amet, consectetur adipisicing elit, sed do eiusmod tempor incididunt ut labore et dolore magna aliqua. Ut enim ad minim veniam, quis nostrud exercitation ullamco laboris nisi ut aliquip ex ea commodo consequat. Duis aute irure dolor in reprehenderit in voluptate velit esse cillum dolore eu fugiat nulla pariatur. Excepteur sint occaecat cupidatat non proident, sunt in culpa qui officia deserunt mollit anim id est laborum.</p>
    <p>Lorem ipsum dolor sit amet, consectetur adipisicing elit, sed do eiusmod tempor incididunt ut labore et dolore magna aliqua. Ut enim ad minim veniam, quis nostrud exercitation ullamco laboris nisi ut aliquip ex ea commodo consequat. Duis aute irure dolor in reprehenderit in voluptate velit esse cillum dolore eu fugiat nulla pariatur. Excepteur sint occaecat cupidatat non proident, sunt in culpa qui officia deserunt mollit anim id est laborum.</p>
    <p>Lorem ipsum dolor sit amet, consectetur adipisicing elit, sed do eiusmod tempor incididunt ut labore et dolore magna aliqua. Ut enim ad minim veniam, quis nostrud exercitation ullamco laboris nisi ut aliquip ex ea commodo consequat. Duis aute irure dolor in reprehenderit.</p>
    <p class="closing">Yours Sincerely,</p>
  </div>
  <div class="signature" role="img" aria-label="Handwritten signature of the sender"></div>

  <ul class="contact contact--footer">
    <li><svg class="icon"><use href="#i-phone"/></svg>+15550142788</li>
    <li><svg class="icon"><use href="#i-mail"/></svg>hello@brightwellcompany.com</li>
    <li><svg class="icon"><use href="#i-web"/></svg>www.brightwellcompany.com</li>
  </ul>
  <address class="address-footer"><strong>Brightwell+Company</strong><br>48 Larkspur Lane,<br>Fernvale, ON K2P 4R7</address>
</section>
</body>
</html>
```